Business Card for Start Up Real Estate Company

We need a business card designed for a new real estate company called Lumivane. We plan on improving the experience of real estate transactions for both consumers and agents by using current and evolving technology. We would like to see designs that use our existing logo (attached). Please use a primarily white or light colored background. The final design should communicate technology, sophistication and customer service. Thank you...

Industry/Entity Type

Real Estate

Requirements
Must have
• Primarily white or light colored background
Nice to have
• Isolated A from our logo used as part of the design
Should not have
• Pictures, especially of houses

```html
<!DOCTYPE html>
<html lang="en">
<head>
<meta charset="utf-8">
<title>Lumivane Business Card</title>
<link rel="stylesheet" href="https://fonts.googleapis.com/css2?family=Source+Sans+3:wght@400;600&display=swap">
<style>
  :root {
    --page-bg: #e9e4da;
    --card-bg: #ffffff;
    --brand-blue: #0b5a9a;
    --brand-red: #e81e3f;
    --text-blue: #0b4f8a;
  }
  * { margin: 0; padding: 0; box-sizing: border-box; }
  html, body {
    width: 1200px; height: 1000px; overflow: hidden;
    background: var(--page-bg);
    font-family: "Source Sans 3", Arial, sans-serif;
  }
  .card {
    position: absolute; left: 100px; top: 193px;
    width: 1000px; height: 614px;
    background: var(--card-bg);
    border-radius: 30px;
    overflow: hidden;
    box-shadow: 0 4px 14px rgba(0,0,0,0.12);
  }
  .brand-name {
    position: absolute; left: 49px; top: 46px;
    font-size: 60px; font-weight: 400; letter-spacing: 2px;
    color: var(--brand-blue); line-height: 1;
  }
  .holder {
    position: absolute; left: 0; width: 880px; top: 212px;
    text-align: center; color: var(--text-blue);
  }
  .holder-name { font-size: 42px; font-weight: 400; line-height: 1.1; }
  .holder-title { font-size: 27px; font-weight: 400; margin-top: 4px; }
  .contact { position: absolute; color: var(--text-blue); font-size: 21px; font-weight: 600; }
  .contact-row { position: absolute; display: flex; align-items: flex-start; white-space: nowrap; }
  .contact-row svg { width: 24px; height: 24px; flex: none; margin-top: 5px; }
  .contact-row span { margin-left: 14px; line-height: 34px; }
  .contact-right .contact-row span { font-weight: 400; font-size: 22px; }
  .contact-left { left: 47px; top: 404px; }
  .contact-right { left: 487px; top: 404px; }
  .corner-accent {
    position: absolute; right: 0; top: 174px;
    width: 230px; height: 440px;
    background: linear-gradient(160deg, var(--brand-blue) 0%, #5a4f8e 55%, var(--brand-red) 100%);
    opacity: 0.9;
  }
</style>
</head>
<body>
  <div class="card">
    <div class="brand-name">LUMIVANE</div>

    <div class="holder">
      <div class="holder-name">Firstname J.Lastname</div>
      <div class="holder-title">Your job Title</div>
    </div>

    <div class="contact contact-left">
      <div class="contact-row" style="top:0">
        <svg viewBox="0 0 24 24" fill="none" stroke="var(--brand-red)" stroke-width="1.8"><path d="M12 22s7-7.5 7-13a7 7 0 0 0-14 0c0 5.5 7 13 7 13z"/><circle cx="12" cy="9" r="2.5"/></svg>
        <span>12345 Your Street Adress, Town,<br>State , Country, Zip 90210</span>
      </div>
      <div class="contact-row" style="top:101px">
        <svg viewBox="0 0 24 24" fill="none" stroke="var(--brand-red)" stroke-width="1.8"><circle cx="12" cy="10" r="7"/><path d="M12 17v5M8 22h8"/></svg>
        <span>www.yoursiteweb.com</span>
      </div>
    </div>

    <div class="contact contact-right">
      <div class="contact-row" style="top:0">
        <svg viewBox="0 0 24 24" fill="none" stroke="var(--brand-red)" stroke-width="1.8"><path d="M5 3h4l2 5-2.5 1.5a11 11 0 0 0 6 6L16 13l5 2v4a2 2 0 0 1-2 2A16 16 0 0 1 3 5a2 2 0 0 1 2-2z"/></svg>
        <span>012 345 6789</span>
      </div>
      <div class="contact-row" style="top:34px">
        <svg viewBox="0 0 24 24" fill="none" stroke="var(--brand-red)" stroke-width="1.8"><rect x="7" y="2" width="10" height="20" rx="2"/><path d="M11 18h2"/></svg>
        <span>012 345 6789</span>
      </div>
      <div class="contact-row" style="top:68px">
        <svg viewBox="0 0 24 24" fill="none" stroke="var(--brand-red)" stroke-width="1.8"><rect x="3" y="10" width="18" height="10" rx="1"/><path d="M7 10V3h10v7M7 15h10"/></svg>
        <span>012 345 6789</span>
      </div>
      <div class="contact-row" style="top:101px">
        <svg viewBox="0 0 24 24" fill="none" stroke="var(--brand-red)" stroke-width="1.8"><rect x="2" y="5" width="20" height="14" rx="1"/><path d="M2 6l10 7 10-7"/></svg>
        <span>mail@yoursiteweb.com</span>
      </div>
    </div>

    <div class="corner-accent" role="img" aria-label="Brand accent graphic in blue and red"></div>
  </div>
</body>
</html>
```